Crestline Alloy Partners Business Card

Design a business card for a new company. Crestline Alloy Partners is a subsidiary of KVT, Inc. (www.kvtreclaims.example)

Target Market(s)

B2B, Manufactures

Industry/Entity Type

Recycling

Contact Information for Business Card

Crestline Alloy Partners, LLC.
40517 West Fennimore Lane
Dorwick IL 60594
P: (555) 309-4462
F: (555) 309-4461
www.crestap.example
Email@crestap.example

Font styles to use
Sans Serif

Requirements
Must have
• A KVT, Inc. subsidiary company.
Nice to have
• Recycling Solutions. Uncompromised. (slogan)

```html
<!DOCTYPE html>
<html lang="en">
<head>
<meta charset="utf-8">
<title>Crestline Alloy Partners – Business Card</title>
<link rel="stylesheet" href="https://fonts.googleapis.com/css2?family=Source+Sans+3:ital,wght@0,400;0,600;0,700;1,600&display=swap">
<style>
  :root {
    --stage-top: #2a2a2a;
    --stage-bottom: #050505;
    --card-light: #f2f2f2;
    --ink: #1a1a1a;
    --navy: #1c3a7e;
    --teal: #1b6f90;
    --brand: #1f4a8c;
    --icon: #2d5ea8;
    --blue-core: #52c3ea;
    --blue-mid: #1f6fc0;
    --blue-edge: #172f7c;
    --white: #ffffff;
  }
  * { margin: 0; padding: 0; box-sizing: border-box; }
  html, body { width: 1200px; height: 900px; overflow: hidden; }
  body {
    position: relative;
    background: linear-gradient(180deg, var(--stage-top) 0%, #161616 55%, var(--stage-bottom) 100%);
    font-family: "Source Sans 3", "Myriad Pro", Arial, sans-serif;
  }
  .card {
    position: absolute;
    top: 184px;
    height: 490px;
    border-radius: 12px;
    overflow: hidden;
    box-shadow: 0 4px 14px rgba(0,0,0,.55);
  }
  .card-front { left: 299px; width: 301px; background: var(--card-light); color: var(--ink); }
  .card-back {
    left: 645px; width: 304px; color: var(--white);
    background: radial-gradient(ellipse 62% 52% at 50% 48%, var(--blue-core) 0%, var(--blue-mid) 48%, var(--blue-edge) 100%);
  }
  .brand-name {
    position: absolute; left: 0; right: 0;
    text-align: center; font-weight: 700; line-height: 1.05;
  }
  .card-front .brand-name { top: 76px; font-size: 30px; color: var(--brand); }
  .card-back .brand-name { top: 192px; font-size: 31px; color: var(--white); }
  .contact-list {
    position: absolute; top: 239px; left: 0; right: 0;
    list-style: none; text-align: center; font-size: 14px; line-height: 20px;
  }
  .contact-list li { display: flex; justify-content: center; align-items: center; gap: 5px; }
  .contact-list svg { width: 10px; height: 10px; fill: var(--icon); flex: none; }
  .address {
    position: absolute; top: 347px; left: 0; right: 0;
    text-align: center; font-size: 14px; line-height: 20px; font-style: normal;
  }
  .slogan {
    position: absolute; top: 408px; left: 0; right: 0;
    text-align: center; font-size: 17.5px; font-style: italic; font-weight: 600; line-height: 24px;
  }
  .slogan .line-one { color: var(--navy); display: block; }
  .slogan .line-two { color: var(--teal); display: block; }
  .parent-note {
    position: absolute; top: 387px; left: 0; right: 0;
    text-align: center; font-size: 13.5px; line-height: 21px;
  }
  .parent-url {
    position: absolute; top: 440px; left: 0; right: 0;
    text-align: center; font-size: 13.5px; font-weight: 700;
  }
</style>
</head>
<body>
  <section class="card card-front" aria-label="Card front">
    <div class="brand-name">Crestline<br>Alloy Partners</div>
    <ul class="contact-list">
      <li><svg viewBox="0 0 10 10" aria-hidden="true"><path d="M2 0.5 3.8 2.6 2.9 3.7C3.6 5 4.8 6.3 6.2 7L7.3 6.1 9.5 8 8.4 9.4C4.6 9.2 0.8 5.4 0.6 1.6Z"/></svg>(555) 309-4462</li>
      <li><svg viewBox="0 0 10 10" aria-hidden="true"><rect x="0.5" y="3" width="9" height="6.5" rx="1"/><rect x="2.5" y="0.5" width="5" height="3" fill="#8fb0da"/><rect x="2.5" y="5" width="5" height="1" fill="#fff"/></svg>(555) 309-4461</li>
      <li><svg viewBox="0 0 10 10" aria-hidden="true"><rect x="0.5" y="2" width="9" height="6.5"/><path d="M0.8 2.3 5 5.6 9.2 2.3" fill="none" stroke="#fff" stroke-width="0.9"/></svg>Email@crestap.example</li>
      <li><svg viewBox="0 0 10 10" aria-hidden="true"><path d="M4.2 5.8 5.8 4.2M3.6 4.4 2 6a1.4 1.4 0 0 0 2 2l1.6-1.6M6.4 5.6 8 4a1.4 1.4 0 0 0-2-2L4.4 3.6" fill="none" stroke="#2d5ea8" stroke-width="1.2" stroke-linecap="round"/></svg>www.crestap.example</li>
    </ul>
    <address class="address">40517 West Fennimore<br>Lane Dorwick IL 60594</address>
    <p class="slogan"><span class="line-one">Recycling Solutions</span><span class="line-two">Uncompromised</span></p>
  </section>

  <section class="card card-back" aria-label="Card back">
    <div class="brand-name">Crestline<br>Alloy Partners</div>
    <p class="parent-note">Crestline Alloy Partners is a subsidiary of<br>KVT, Inc.</p>
    <p class="parent-url">www.kvtreclaims.example</p>
  </section>
</body>
</html>
```